Packaging for new retail dips "Quorlets"

* We require packaging for our new retail dip range.
* We have a small "Our Story" write up that we would like somewhere...
* We have approx. 7 different flavours - Hommous, Mediterranean Olive, Beetroot, Tzatziki etc. We would like one design where we can change the colour panel and the name of the dip.
* We are looking for a modern, clean, gourmet looking design - not the usual dip packaging you see on supermarket shelves.
* See my inspiration photo's.
* The Dieline attached is to scale.
Updates
Project Deadline Extended
Reason: Extension due to Dielines and Measurements not uploaded when we thought they were.
Target Market(s)
Will be going into retail supermarkets.
Industry/Entity Type
Retail
Font styles to use
Colors
Designer to choose colors to be used in the design.
Requirements
Must have
- * Please use our 'Quorlets' logo on the front and on the front side (if possible).
Nice to have
- * 'taste is everything' somewhere...
Should not have
- * No photo's of dips or photo's in general.

```html
<!DOCTYPE html>
<html lang="en">
<head>
<meta charset="utf-8">
<title>Quorlets – Dip Packaging</title>
<link rel="stylesheet" href="https://fonts.googleapis.com/css2?family=Josefin+Sans:wght@300;400&family=Lobster&family=Oswald:wght@500&family=Quicksand:wght@400;500&display=swap">
<style>
  :root{
    --bg:#e7e7e9;
    --white:#ffffff;
    --ink:#2b2b2b;
    --hommous:#668c1f;
    --hommous-frame:#4f6a23;
    --olive:#d38a05;
    --olive-frame:#a8661b;
    --beet:#8a0f52;
    --beet-frame:#6b1a43;
    --muted:#8a8a8a;
  }
  *{box-sizing:border-box;margin:0;padding:0}
  html,body{width:1200px;height:1200px;overflow:hidden}
  body{
    background:radial-gradient(circle at 50% 30%, #f6f6f7 0%, var(--bg) 75%);
    font-family:"Quicksand",sans-serif;color:var(--ink);
    position:relative;
  }

  /* brand name */
  .brand{text-align:center;line-height:1}
  .brand__name{font-family:"Quicksand",sans-serif;font-weight:500;letter-spacing:.01em;color:var(--ink)}
  .brand--corner{position:absolute;top:160px;right:70px}
  .brand--corner .brand__name{font-size:42px}

  /* flavour label */
  .label{
    --accent:var(--hommous);--frame:var(--hommous-frame);
    position:absolute;width:29.5em;height:27.5em;background:var(--white);
    padding:2.6em 2em 2.6em;
    box-shadow:0 .6em 1.6em rgba(0,0,0,.12);
  }
  .label--olive{--accent:var(--olive);--frame:var(--olive-frame)}
  .label--beet{--accent:var(--beet);--frame:var(--beet-frame)}
  .label__frame{
    height:100%;border:.45em solid var(--frame);
    display:flex;flex-direction:column;align-items:center;
    padding-top:6.6em;
  }
  .label .brand__name{font-size:2.3em}
  .label__band{
    align-self:stretch;margin:2.4em 1.2em 0;background:var(--accent);
    color:var(--white);text-align:center;padding:.7em 0 .6em;
  }
  .label__product{font-family:"Josefin Sans",sans-serif;font-size:1.8em;letter-spacing:.12em;line-height:1}
  .label__variant{font-family:"Lobster",cursive;font-size:1.15em;margin-top:.1em}
  .label__rule{width:9em;margin:.25em auto .35em;border-top:.12em dotted rgba(255,255,255,.85)}
  .label__uses{font-size:.75em;opacity:.8;letter-spacing:.05em}
  .label__footer{
    margin-top:auto;align-self:stretch;display:flex;justify-content:space-between;align-items:baseline;
    padding:0 1.2em .5em;
  }
  .label__weight{font-family:"Josefin Sans",sans-serif;font-weight:300;font-size:1.4em;color:var(--muted)}
  .label__flavour{font-size:1em;font-weight:500;color:var(--frame)}
  .tab{
    position:absolute;left:50%;transform:translateX(-50%);
    background:var(--white);padding:.35em 1.4em;border-radius:50%/60%;
    font-family:"Oswald",sans-serif;font-weight:500;font-size:1em;letter-spacing:.04em;
    color:var(--frame);white-space:nowrap;
  }
  .tab--top{top:-.9em}
  .tab--bottom{bottom:-.9em}

  .label--lid{font-size:20px;left:190px;top:40px;width:29.5em;height:28em}
  .label--small{font-size:10px;top:860px}
  .label--small.label--hommous{left:128px}
  .label--small.label--olive{left:452px}
  .label--small.label--beet{left:777px}

  /* side panel */
  .side-panel{
    position:absolute;left:150px;top:640px;width:900px;height:160px;
    display:flex;box-shadow:0 8px 18px rgba(0,0,0,.12);
  }
  .side-panel__brand{width:230px;background:#ececec;display:flex;flex-direction:column;justify-content:center}
  .side-panel__brand .brand__name{font-size:28px}
  .side-panel__story{flex:1;background:var(--hommous);color:var(--white);padding:26px 30px;position:relative}
  .side-panel__story h2{font-family:"Lobster",cursive;font-weight:400;font-size:34px;line-height:1}
  .side-panel__story p{font-family:"Josefin Sans",sans-serif;font-weight:300;font-size:14px;letter-spacing:.1em;line-height:1.25;margin-top:10px;max-width:560px}
  .side-panel .tab{font-size:16px;top:-14px;left:330px;color:var(--hommous-frame);transform:none}
</style>
</head>
<body>
  <div class="brand brand--corner">
    <div class="brand__name">Quorlets</div>
  </div>

  <article class="label label--lid label--hommous">
    <div class="tab tab--top">· TASTE IS EVERYTHING ·</div>
    <div class="label__frame">
      <div class="brand"><div class="brand__name">Quorlets</div></div>
      <div class="label__band">
        <div class="label__product">TARAMASALATA</div>
        <div class="label__variant">Caviar Dip</div>
        <div class="label__rule"></div>
        <div class="label__uses">spread . sauce . dressing</div>
      </div>
      <div class="label__footer"><span class="label__weight">150g</span><span class="label__flavour">Hommous Flavor</span></div>
    </div>
  </article>

  <section class="side-panel">
    <div class="side-panel__brand brand"><div class="brand__name">Quorlets</div></div>
    <div class="side-panel__story">
      <div class="tab">· TASTE IS EVERYTHING ·</div>
      <h2>Our Story</h2>
      <p>Lorem ipsum dolor sit amet, consectetur adipiscing elit, sed do eiusmod tempor incididunt ut labore et dolore magna aliqua. Elementum nisi quis eleifend quam.</p>
    </div>
  </section>

  <article class="label label--small label--hommous">
    <div class="tab tab--top">· TASTE IS EVERYTHING ·</div>
    <div class="label__frame">
      <div class="brand"><div class="brand__name">Quorlets</div></div>
      <div class="label__band"><div class="label__product">TARAMASALATA</div><div class="label__variant">Caviar Dip</div><div class="label__rule"></div><div class="label__uses">spread . sauce . dressing</div></div>
      <div class="label__footer"><span class="label__weight">150g</span><span class="label__flavour">Hommous Flavor</span></div>
    </div>
    <div class="tab tab--bottom">· TASTE IS EVERYTHING ·</div>
  </article>

  <article class="label label--small label--olive">
    <div class="tab tab--top">· TASTE IS EVERYTHING ·</div>
    <div class="label__frame">
      <div class="brand"><div class="brand__name">Quorlets</div></div>
      <div class="label__band"><div class="label__product">TARAMASALATA</div><div class="label__variant">Caviar Dip</div><div class="label__rule"></div><div class="label__uses">spread . sauce . dressing</div></div>
      <div class="label__footer"><span class="label__weight">150g</span><span class="label__flavour">Mediterranean Olive Flavor</span></div>
    </div>
    <div class="tab tab--bottom">· TASTE IS EVERYTHING ·</div>
  </article>

  <article class="label label--small label--beet">
    <div class="tab tab--top">· TASTE IS EVERYTHING ·</div>
    <div class="label__frame">
      <div class="brand"><div class="brand__name">Quorlets</div></div>
      <div class="label__band"><div class="label__product">TARAMASALATA</div><div class="label__variant">Caviar Dip</div><div class="label__rule"></div><div class="label__uses">spread . sauce . dressing</div></div>
      <div class="label__footer"><span class="label__weight">150g</span><span class="label__flavour">Beetroot Flavor</span></div>
    </div>
    <div class="tab tab--bottom">· TASTE IS EVERYTHING ·</div>
  </article>
</body>
</html>
```